New Flyer Design Project

I would like to purchase a customized version of a design you have previously submitted - https://www.brivomart.example/design/58204731

I want this to be something that looks really good.
We use this to explain our service agreements.
our website is www.plorvex.example I want to stick with those colors.

```html
<!DOCTYPE html>
<html lang="en">
<head>
<meta charset="utf-8">
<title>Plorvex – Service Plans Comparison</title>
<link href="https://fonts.googleapis.com/css2?family=Fira+Sans:wght@400;500;600&family=Rajdhani:wght@500;600;700&display=swap" rel="stylesheet">
<style>
  :root {
    --brand-red: #e31e24;
    --brand-grey: #6d6e72;
    --ink: #2b2b2d;
    --row-a: #efeff1;
    --row-b: #f7f7f8;
    --paper: #ffffff;
    --backdrop: #e9e7e4;
  }
  * { box-sizing: border-box; margin: 0; padding: 0; }
  html, body { width: 1200px; height: 1200px; overflow: hidden; }
  body {
    background: var(--backdrop);
    font-family: "Fira Sans", sans-serif;
    color: var(--ink);
    position: relative;
  }
  .flyer {
    position: absolute;
    left: 190px; top: 15px;
    width: 820px; height: 1170px;
    background: var(--paper);
    box-shadow: 0 6px 24px rgba(0,0,0,.18);
    overflow: hidden;
  }
  .flyer-header {
    height: 135px;
    display: flex; align-items: center; justify-content: center; gap: 12px;
    background: linear-gradient(180deg, #ffffff 0%, #f3f3f4 100%);
  }
  .brand-name {
    font-family: "Rajdhani", sans-serif;
    font-weight: 700; font-size: 54px; letter-spacing: 3px;
    color: var(--brand-grey);
  }
  .brand-dot { width: 18px; height: 18px; border-radius: 50%; background: var(--brand-red); }
  .title-band { position: relative; height: 82px; }
  .title-band .rule-top {
    position: absolute; left: 0; top: 0; width: 265px; height: 6px; background: var(--brand-grey);
  }
  .title-band .band {
    position: absolute; left: 0; right: 0; top: 6px; height: 66px;
    background: var(--brand-red);
    display: flex; align-items: center; justify-content: center;
  }
  .title-band h1 {
    font-family: "Rajdhani", sans-serif;
    font-weight: 500; font-size: 54px; letter-spacing: 1px;
    color: #fff; text-transform: uppercase;
  }
  .title-band .rule-bottom {
    position: absolute; right: 0; top: 72px; width: 250px; height: 6px; background: var(--brand-grey);
  }
  .plans { position: absolute; left: 64px; right: 56px; top: 238px; }
  .plan-heads {
    display: grid; grid-template-columns: 420px 150px 150px; column-gap: 5px;
  }
  .plan-head {
    height: 64px; border-radius: 8px 8px 0 0;
    color: #fff; text-align: center;
    font-weight: 600; font-size: 17px; line-height: 22px;
    display: flex; flex-direction: column; justify-content: center;
  }
  .plan-head.security { background: var(--brand-red); }
  .plan-head.essentials { background: var(--brand-grey); }
  .feature-table { display: grid; grid-template-columns: 420px 150px 150px; column-gap: 5px; row-gap: 5px; }
  .feature-table > div {
    height: 38px; display: flex; align-items: center; font-size: 15px;
  }
  .feature-table .label { padding-left: 12px; font-weight: 500; }
  .feature-table .mark { justify-content: center; }
  .feature-table .odd { background: var(--row-a); }
  .feature-table .even { background: var(--row-b); }
  .tick { width: 16px; height: 16px; }
  .tick.red circle { fill: var(--brand-red); }
  .tick.grey circle { fill: var(--brand-grey); }
  .tick path { fill: none; stroke: #fff; stroke-width: 2.4; stroke-linecap: round; stroke-linejoin: round; }
  .available { font-size: 15px; }
  .flyer-footer {
    position: absolute; left: 0; right: 0; bottom: 30px;
    text-align: center; font-size: 17px; font-weight: 500;
  }
  .flyer-footer .cta { color: var(--brand-red); }
  .flyer-footer .url { color: var(--brand-grey); font-weight: 600; }
  .footer-band { position: absolute; left: 0; right: 0; bottom: 0; height: 14px; background: #8f9094; }
</style>
</head>
<body>
<main class="flyer">
  <header class="flyer-header">
    <span class="brand-name">PLORVEX</span>
    <span class="brand-dot"></span>
  </header>

  <section class="title-band">
    <div class="rule-top"></div>
    <div class="band"><h1>Service Plans Compairson</h1></div>
    <div class="rule-bottom"></div>
  </section>

  <section class="plans">
    <div class="plan-heads">
      <div></div>
      <div class="plan-head security"><span>SECURITY PLUS</span><span>$75.00</span></div>
      <div class="plan-head essentials"><span>IT ESSENTIALS</span><span>$55.00/PC</span></div>
    </div>

    <svg width="0" height="0" style="position:absolute">
      <defs>
        <symbol id="tick" viewBox="0 0 16 16"><circle cx="8" cy="8" r="8"/><path d="M4.6 8.3l2.2 2.2 4.4-4.6"/></symbol>
      </defs>
    </svg>

    <div class="feature-table">
      <div class="label odd">Unlimited US bases Remote Help Desk Support</div>
      <div class="mark odd"><svg class="tick red"><use href="#tick"/></svg></div>
      <div class="mark odd"><svg class="tick grey"><use href="#tick"/></svg></div>

      <div class="label even">Unlimited On-Site Support</div>
      <div class="mark even"><svg class="tick red"><use href="#tick"/></svg></div>
      <div class="mark even"><span class="available">Available</span></div>

      <div class="label odd">Advanced Cybersecurity and Threat Hunting</div>
      <div class="mark odd"><svg class="tick red"><use href="#tick"/></svg></div>
      <div class="mark odd"><span class="available">Available</span></div>

      <div class="label even">Managed Antivirus Protection</div>
      <div class="mark even"><svg class="tick red"><use href="#tick"/></svg></div>
      <div class="mark even"><svg class="tick grey"><use href="#tick"/></svg></div>

      <div class="label odd">Multifactor Authentication Powered by Keyvant</div>
      <div class="mark odd"><svg class="tick red"><use href="#tick"/></svg></div>
      <div class="mark odd"><span class="available">Available</span></div>

      <div class="label even">Cyber Security Awareness Training</div>
      <div class="mark even"><svg class="tick red"><use href="#tick"/></svg></div>
      <div class="mark even"><span class="available">Available</span></div>

      <div class="label odd">Enhanced Span Filtering</div>
      <div class="mark odd"><svg class="tick red"><use href="#tick"/></svg></div>
      <div class="mark odd"><span class="available">Available</span></div>

      <div class="label even">Internet Content Filtering</div>
      <div class="mark even"><svg class="tick red"><use href="#tick"/></svg></div>
      <div class="mark even"><span class="available">Available</span></div>

      <div class="label odd">Proactive Security and System Monitoring</div>
      <div class="mark odd"><svg class="tick red"><use href="#tick"/></svg></div>
      <div class="mark odd"><svg class="tick grey"><use href="#tick"/></svg></div>

      <div class="label even">Security and Vulnerability patching</div>
      <div class="mark even"><svg class="tick red"><use href="#tick"/></svg></div>
      <div class="mark even"><svg class="tick grey"><use href="#tick"/></svg></div>

      <div class="label odd">Backup and disaster recovery</div>
      <div class="mark odd"><svg class="tick red"><use href="#tick"/></svg></div>
      <div class="mark odd"><svg class="tick grey"><use href="#tick"/></svg></div>

      <div class="label even">Network Management and Administration</div>
      <div class="mark even"><svg class="tick red"><use href="#tick"/></svg></div>
      <div class="mark even"><svg class="tick grey"><use href="#tick"/></svg></div>

      <div class="label odd">Vantora Office Suite Administration and Configuration</div>
      <div class="mark odd"><svg class="tick red"><use href="#tick"/></svg></div>
      <div class="mark odd"><svg class="tick grey"><use href="#tick"/></svg></div>

      <div class="label even">Vantora Cloud Administration and Configuration</div>
      <div class="mark even"><svg class="tick red"><use href="#tick"/></svg></div>
      <div class="mark even"><svg class="tick grey"><use href="#tick"/></svg></div>

      <div class="label odd">Vantora Desktop and Server Support</div>
      <div class="mark odd"><svg class="tick red"><use href="#tick"/></svg></div>
      <div class="mark odd"><svg class="tick grey"><use href="#tick"/></svg></div>

      <div class="label even">Managed DNS</div>
      <div class="mark even"><svg class="tick red"><use href="#tick"/></svg></div>
      <div class="mark even"><svg class="tick grey"><use href="#tick"/></svg></div>

      <div class="label odd">Hardware and Software Procurement</div>
      <div class="mark odd"><svg class="tick red"><use href="#tick"/></svg></div>
      <div class="mark odd"><svg class="tick grey"><use href="#tick"/></svg></div>

      <div class="label even">Assett Management</div>
      <div class="mark even"><svg class="tick red"><use href="#tick"/></svg></div>
      <div class="mark even"><svg class="tick grey"><use href="#tick"/></svg></div>
    </div>
  </section>

  <footer class="flyer-footer">
    <span class="cta">Are You Having A Technology Emergency? We Can Help Contact Us Now</span>
    <span class="url">www.plorvex.example</span>
  </footer>
  <div class="footer-band"></div>
</main>
</body>
</html>
```